Business Card for premium dental clinic

We are a premium dental clinic based in Brasov, Romania with more than 15 year on the market, providing quality dental treatment made by a team of more specialized dentists, working with modern equipment as a solution to beautiful and healthy teeth.

Our current logo for the clinic use 2 square with colors black and gold - dr Merinca - studio, using family fonts Bodoni, Myriad Pro and Segoe Print.
Depending on the printing we used some gold CMYK background or gold foil picture background or a gold gradient.
We want a business card:
- eye catching business card
- distinguished business card
- premium design
- to keep the color scheme of black and gold
- to attract the customers to spent time reading the information
- modern concept

```html
<!DOCTYPE html>
<html lang="en">
<head>
<meta charset="utf-8">
<title>Business cards – dr Merinca studio</title>
<link rel="stylesheet" href="https://fonts.googleapis.com/css2?family=Montserrat:wght@400;500;600;700&display=swap">
<style>
  :root{
    --stage:#2b2c2e;
    --card-dark:#232526;
    --card-dark-2:#303335;
    --ink:#111;
    --paper:#f4f4f2;
    --gold:#c9a227;
    --gold-light:#e0bd45;
    --text-light:#e9e9e9;
  }
  *{margin:0;padding:0;box-sizing:border-box}
  html,body{width:1200px;height:866px;overflow:hidden}
  body{background:var(--stage);font-family:"Montserrat",sans-serif;position:relative}

  .card{position:absolute;width:620px;height:354px;border-radius:4px;overflow:hidden;box-shadow:0 14px 30px rgba(0,0,0,.45)}

  /* back of card */
  .card--back{left:60px;top:60px;background:linear-gradient(160deg,var(--card-dark-2),var(--card-dark))}
  .back-frame{position:absolute;inset:26px;border:6px solid var(--gold)}
  .back-logo{position:absolute;left:50%;top:50%;transform:translate(-50%,-50%)}

  /* logo replacement lockup */
  .brand{display:flex;align-items:center;gap:14px;background:var(--ink);border:2px solid #fff;padding:18px 26px}
  .brand-mark{width:40px;height:40px;background:var(--gold)}
  .brand-name{font-weight:600;font-size:24px;color:var(--gold-light);letter-spacing:.5px;white-space:nowrap}

  /* front of card */
  .card--front{left:520px;top:452px;background:var(--paper)}
  .front-logo{position:absolute;left:50%;top:92px;transform:translate(-50%,-50%)}
  .front-band{position:absolute;left:0;right:0;bottom:0;height:170px;background:var(--card-dark);border-top:6px solid var(--gold);display:flex;align-items:center;padding:0 36px}
  .person{flex:0 0 262px;text-align:right;padding-right:24px}
  .person-name{font-weight:700;font-size:24px;color:var(--gold)}
  .person-role{font-weight:500;font-size:17px;color:var(--text-light);margin-top:2px}
  .person-address{font-size:13px;color:var(--text-light);margin-top:10px;line-height:1.45}
  .divider{width:2px;height:84px;background:var(--gold);margin-right:26px}
  .contacts{list-style:none;display:flex;flex-direction:column;gap:12px}
  .contact{display:flex;align-items:center;gap:12px;font-size:14px;color:var(--text-light)}
  .contact svg{width:15px;height:15px;flex:0 0 15px;fill:var(--gold)}
</style>
</head>
<body>

<section class="card card--back" aria-label="Business card back">
  <div class="back-frame"></div>
  <div class="back-logo brand">
    <span class="brand-mark"></span>
    <span class="brand-name">dr. Merinca studio</span>
  </div>
</section>

<section class="card card--front" aria-label="Business card front">
  <div class="front-logo brand">
    <span class="brand-mark"></span>
    <span class="brand-name">dr. Merinca studio</span>
  </div>
  <div class="front-band">
    <div class="person">
      <p class="person-name">Andra Dobrescu</p>
      <p class="person-role">Doctor</p>
      <p class="person-address">Strada Lunga nr 24<br>500058 Brașov</p>
    </div>
    <div class="divider"></div>
    <ul class="contacts">
      <li class="contact">
        <svg viewBox="0 0 24 24" aria-hidden="true"><path d="M6.6 10.8a15.1 15.1 0 0 0 6.6 6.6l2.2-2.2c.3-.3.7-.4 1-.2 1.1.4 2.3.6 3.6.6.6 0 1 .4 1 1V20c0 .6-.4 1-1 1A17 17 0 0 1 3 4c0-.6.4-1 1-1h3.5c.6 0 1 .4 1 1 0 1.3.2 2.5.6 3.6.1.3 0 .7-.2 1z"/></svg>
        <span>+40 268 555 019</span>
      </li>
      <li class="contact">
        <svg viewBox="0 0 24 24" aria-hidden="true"><path d="M2 5h20v14H2zm2 2v.4l8 5 8-5V7l-8 5z"/></svg>
        <span>a.dobrescu@drmerinca.ro</span>
      </li>
      <li class="contact">
        <svg viewBox="0 0 24 24" aria-hidden="true"><path d="M12 2a10 10 0 1 0 0 20 10 10 0 0 0 0-20zm6.9 9h-3a15 15 0 0 0-1.3-5.6A8 8 0 0 1 18.9 11zM12 4.1c.9 1.2 1.8 3.6 1.9 6.9h-3.8c.1-3.3 1-5.7 1.9-6.9zM9.4 5.4A15 15 0 0 0 8.1 11h-3a8 8 0 0 1 4.3-5.6zM5.1 13h3a15 15 0 0 0 1.3 5.6A8 8 0 0 1 5.1 13zm6.9 6.9c-.9-1.2-1.8-3.6-1.9-6.9h3.8c-.1 3.3-1 5.7-1.9 6.9zm2.6-1.3a15 15 0 0 0 1.3-5.6h3a8 8 0 0 1-4.3 5.6z"/></svg>
        <span>www.drmerinca.ro</span>
      </li>
    </ul>
  </div>
</section>

</body>
</html>
```